K & R Ground Works. Business card design

We need a business card designed for a new business. We have a bulldozer and tractor service. We clear land and make wildlife food plots. We provide disking, bush hogging, and site prep services.
I have attached an image of a business card that I like and would like my business cards to look similar.

Target Market(s)

anyone needing bulldozer and/or tractor services

Industry/Entity Type

Business

Contact Information for Business Card

K & R Ground Works, Operated by 7-T-Ranch
Dale Whitcomb
601-555-0148
dwk4821@mailbarn.example

Font styles to use
Sans Serif

Colors

Designer to choose colors to be used in the design.

Requirements
Must have
• image of tractor and bulldozer
• Land Clearing
• Wildlife food plots
• Bush Hogging
• Disking
• Site prep
Nice to have
• i have included a image of a business card that i like. I would like mine to be similar.

```html
<!DOCTYPE html>
<html lang="en">
<head>
<meta charset="utf-8">
<title>K &amp; R Ground Works – Business Card</title>
<link href="https://fonts.googleapis.com/css2?family=Mulish:wght@400;600&display=swap" rel="stylesheet">
<style>
  :root {
    --backdrop: #e9eef0;
    --olive-dark: #3b4124;
    --olive-mid: #4a5230;
    --olive-light: #cfd3a6;
    --cream: #f3f1e4;
    --white: #ffffff;
    --sky: #6f9fd6;
    --ground: #b9a98a;
    --grass: #6f7a45;
    --brand-ink: #3b4124;
  }
  html, body {
    margin: 0;
    width: 1200px;
    height: 800px;
    overflow: hidden;
    background: var(--backdrop);
    font-family: "Mulish", Arial, sans-serif;
  }
  .canvas {
    position: relative;
    width: 1200px;
    height: 800px;
  }
  .business-card {
    position: absolute;
    left: 75px;
    top: 100px;
    width: 1050px;
    height: 600px;
    overflow: hidden;
    background: var(--olive-dark);
  }
  .card-art { position: absolute; inset: 0; }
  .brand {
    position: absolute;
    left: 230px;
    top: 48px;
    padding: 10px 26px 12px 18px;
    background: rgba(255,255,255,0.72);
    border-radius: 6px;
  }
  .brand-name {
    display: flex;
    align-items: center;
    gap: 14px;
    margin: 0;
    font-weight: 600;
    font-size: 50px;
    line-height: 1;
    color: var(--brand-ink);
  }
  .brand-dot {
    width: 30px; height: 30px;
    border-radius: 50%;
    background: var(--olive-mid);
  }
  .brand-operator {
    margin: 6px 0 0 44px;
    font-size: 24px;
    letter-spacing: 1px;
    text-transform: uppercase;
    color: var(--olive-dark);
  }
  .owner {
    position: absolute;
    left: 42px;
    top: 428px;
    color: var(--cream);
  }
  .owner-name {
    margin: 0 0 14px;
    font-size: 50px;
    font-weight: 400;
    color: var(--olive-light);
  }
  .contact-line {
    display: flex;
    align-items: center;
    gap: 16px;
    margin: 0 0 6px;
    font-size: 28px;
  }
  .contact-line svg { width: 34px; height: 30px; fill: var(--olive-light); }
  .services {
    position: absolute;
    right: 42px;
    top: 308px;
    margin: 0;
    padding: 0;
    list-style: none;
    text-align: right;
    font-size: 28px;
    line-height: 1.18;
    color: var(--cream);
  }
</style>
</head>
<body>
<div class="canvas">
  <article class="business-card">
    <svg class="card-art" viewBox="0 0 1050 600" width="1050" height="600">
      <defs>
        <linearGradient id="dozer-tone" x1="0" y1="0" x2="0" y2="1">
          <stop offset="0" stop-color="#5d93d4"/>
          <stop offset="0.45" stop-color="#c9d4dc"/>
          <stop offset="0.6" stop-color="#c9a83a"/>
          <stop offset="1" stop-color="#a99a7c"/>
        </linearGradient>
        <linearGradient id="tractor-tone" x1="0" y1="0" x2="0" y2="1">
          <stop offset="0" stop-color="#4d5f33"/>
          <stop offset="0.45" stop-color="#c9582c"/>
          <stop offset="0.7" stop-color="#8a8f55"/>
          <stop offset="1" stop-color="#6d7444"/>
        </linearGradient>
        <clipPath id="photo-area">
          <polygon points="0,0 1050,0 1050,205 560,395 0,395"/>
        </clipPath>
      </defs>
      <g clip-path="url(#photo-area)">
        <rect class="photo-dozer" x="0" y="0" width="560" height="400" fill="url(#dozer-tone)" role="img" aria-label="Photo of a yellow bulldozer clearing ground under a blue sky"/>
        <polygon class="photo-tractor" points="470,0 1050,0 1050,400 560,400" fill="url(#tractor-tone)" role="img" aria-label="Photo of an orange tractor with front loader bucket in tall grass"/>
      </g>
      <polygon class="service-panel" points="560,395 1050,205 1050,600 560,600" fill="#434a2a"/>
      <line x1="0" y1="397" x2="560" y2="397" stroke="#ffffff" stroke-width="5"/>
      <line x1="560" y1="397" x2="1050" y2="207" stroke="#ffffff" stroke-width="5"/>
    </svg>

    <header class="brand">
      <h1 class="brand-name"><span class="brand-dot"></span>K &amp; R Ground Works</h1>
      <p class="brand-operator">Operated by 7-T-Ranch</p>
    </header>

    <section class="owner">
      <h2 class="owner-name">Dale Whitcomb</h2>
      <p class="contact-line">
        <svg viewBox="0 0 24 22" aria-hidden="true"><path d="M2 6c0-2 3-4 10-4s10 2 10 4v2h-5V6H7v2H2zM6 9h12l3 11H3zM12 11a3 3 0 1 0 0 6 3 3 0 0 0 0-6z"/></svg>
        601-555-0148
      </p>
      <p class="contact-line">
        <svg viewBox="0 0 24 18" aria-hidden="true"><path d="M1 1h22v16H1zM3 3v1l9 6 9-6V3z"/></svg>
        dwk4821@mailbarn.example
      </p>
    </section>

    <ul class="services">
      <li>Land Clearing</li>
      <li>Wildlife food plots</li>
      <li>Bush Hogging</li>
      <li>Disking</li>
      <li>Site prep</li>
    </ul>
  </article>
</div>
</body>
</html>
```